Specialized Personal Trainer Needs a Business Card Design

I need a business card design for my personal training business called Tall Oak Fitness. I have my Human Kinetics degree in Exercise Science from the Halvern Ridge University as well as an extra certification from NBEP (National Board of Exercise Practice). I work as a Cardiac Rehab Exercise Specialist and personal trainer giving specialized exercise prescriptions to those that have different heart conditions as well as work with the general population in weight loss, strength and conditioning, getting/staying fit.
Updates

I decided that I wanted a logo (as I did not have one before I submitted my project for a business card) so I am submitting a project to get a logo done and then I will decide on a business card, hopefully being able to use one of the designs already submitted.  My apologies for doing this backwards.  I am new to this so I appreciate your patience.

Thank you.

Hi, I have just created a project for a logo design (I realized I needed a logo and I should've done that first..oops!), please feel free to participate.  Once I receive a logo I like I will finalize my business card project and hopefully incorporate it into one of your business card designs. 

Thank you!

Target Market(s)

Business professionals

Industry/Entity Type

Personal Trainer

Requirements
Must have
• My name with my info:
Celia R. Dunhill (BHK)
NBEP Certified Clinical Exercise Specialist & Personal Trainer
celia.dunhill@talloakfitness.example
Cell: 604-358-4170

Please make it double sided.
Nice to have
• An image that represents cardiac and general fitness training.

```html
<!DOCTYPE html>
<html lang="en">
<head>
<meta charset="utf-8">
<title>Tall Oak Fitness — Business Card</title>
<link rel="stylesheet" href="https://fonts.googleapis.com/css2?family=Jost:wght@400;500&family=Arimo:wght@400&display=swap">
<style>
  :root {
    --page-bg: #e9e6e1;
    --card-black: #050505;
    --accent-yellow: #d2d000;
    --name-grey: #d9d9d9;
    --text-light: #e8e8e8;
    --ink: #0a0a0a;
    --night-blue: #0b1530;
    --deep-navy: #050a1c;
    --vessel-violet: #6a4fa0;
    --heart-red: #d8456e;
  }
  * { box-sizing: border-box; margin: 0; padding: 0; }
  html, body { width: 1200px; height: 880px; overflow: hidden; }
  body {
    background: var(--page-bg);
    font-family: "Jost", "Futura", sans-serif;
  }
  .sheet {
    width: 1200px; height: 880px;
    display: flex; flex-direction: column;
    align-items: center; justify-content: center;
    gap: 50px;
  }
  .card {
    position: relative;
    width: 630px; height: 360px;
    overflow: hidden;
    box-shadow: 0 6px 18px rgba(0,0,0,0.25);
  }

  /* Back side: artwork with brand band */
  .card-back {
    background: var(--deep-navy);
  }
  .cardio-art {
    position: absolute; inset: 0;
    background:
      radial-gradient(ellipse 22% 30% at 48% 52%, var(--heart-red) 0%, rgba(216,69,110,0.55) 45%, transparent 100%),
      radial-gradient(ellipse 55% 45% at 50% 45%, rgba(106,79,160,0.55) 0%, transparent 100%),
      radial-gradient(ellipse 30% 25% at 15% 20%, rgba(90,130,210,0.45) 0%, transparent 100%),
      radial-gradient(ellipse 35% 30% at 85% 85%, rgba(90,130,210,0.35) 0%, transparent 100%),
      linear-gradient(135deg, var(--night-blue), var(--deep-navy));
  }
  .brand-band {
    position: absolute;
    right: 0; bottom: 0;
    width: 58px; height: 215px;
    background: var(--accent-yellow);
    display: flex; align-items: center; justify-content: center;
  }
  .brand-name {
    transform: rotate(-90deg);
    white-space: nowrap;
    font-family: "Arimo", "Arial", sans-serif;
    font-size: 25px;
    color: var(--ink);
  }

  /* Front side: name and contact */
  .card-front {
    background: var(--card-black);
  }
  .identity {
    position: absolute;
    left: 38px; top: 138px;
    display: flex; align-items: center;
  }
  .person-name {
    font-size: 25px; font-weight: 400;
    letter-spacing: 0.5px;
    color: var(--name-grey);
    text-transform: uppercase;
    white-space: nowrap;
  }
  .divider {
    width: 2px; height: 46px;
    background: var(--accent-yellow);
    margin: 0 12px 0 14px;
  }
  .credential {
    font-size: 12.5px; line-height: 1.3;
    color: var(--text-light);
  }
  .contact-block {
    position: absolute;
    left: 24px; bottom: 36px;
    background: var(--accent-yellow);
    padding: 8px 26px 6px 10px;
    color: var(--ink);
    font-size: 18px; line-height: 1.15;
  }
</style>
</head>
<body>
  <main class="sheet">
    <section class="card card-back">
      <div class="cardio-art" role="img" aria-label="Illustration of a glowing human heart with branching blood vessels on a dark blue background"></div>
      <div class="brand-band">
        <span class="brand-name">Tall Oak Fitness</span>
      </div>
    </section>

    <section class="card card-front">
      <div class="identity">
        <h1 class="person-name">Celia R. Dunhill (BHK)</h1>
        <span class="divider"></span>
        <p class="credential">NBEP Certified Clinical Exercise<br>Specialist &amp; Personal Trainer</p>
      </div>
      <address class="contact-block" style="font-style: normal;">
        celia.dunhill@talloakfitness.example<br>
        Cell: 604-358-4170
      </address>
    </section>
  </main>
</body>
</html>
```